Kiosk Coin Venture: Safe and Secure Cash Money

Front of card: LOGO

Back of card:
$$$ FREE ATM PLACEMENT $$$
BENIFITS OF HAVING AN ATM AT YOUR BUSINESS
FREE ATM and BTM (Bitcoin) installation, maintenance, and loading.
Lower card processing fees
Stimulate more traffic.
Ease of access for customers
Maintain customers inside location.
Higher tips and spending

Contact me for more information!
Name: Tobias Merlano
Phone: (512) 638-9071 - Call or Text
Email: Tobias@KioskCoin.example

Contact Information for Business Card

The card should be shape of the logo. Only the back will have all the contact and business details.

Requirements
Must have
• The logo itself will be one side, the card will be the shape of the logo. contact details on back side.

```html
<!DOCTYPE html>
<html lang="en">
<head>
<meta charset="utf-8">
<title>Kiosk Coin Venture – Business Card</title>
<link rel="stylesheet" href="https://fonts.googleapis.com/css2?family=Montserrat:wght@400;500;700;800&display=swap">
<style>
  :root {
    --page-bg: #ececec;
    --card-white: #ffffff;
    --ink: #111111;
    --ink-soft: #1c1c1c;
    --brand-grey: #6b6b6b;
    --silver-1: #b9b9b9;
    --silver-2: #ebebeb;
    --silver-3: #a4a4a4;
    --silver-4: #f4f4f4;
    --card-shadow: rgba(0, 0, 0, 0.18);
  }
  * { box-sizing: border-box; margin: 0; padding: 0; }
  html, body {
    width: 1200px;
    height: 1200px;
    overflow: hidden;
    background: var(--page-bg);
    font-family: "Montserrat", Arial, sans-serif;
    color: var(--ink);
  }
  .sheet { position: relative; width: 1200px; height: 1200px; }
  .card {
    position: absolute;
    top: 181px;
    width: 493px;
    height: 840px;
    background: var(--card-white);
    box-shadow: 0 2px 6px var(--card-shadow);
    overflow: hidden;
  }
  .card--front { left: 91px; }
  .card--back { left: 619px; }

  /* Front */
  .brand-mark {
    position: absolute;
    top: 120px;
    left: 0;
    width: 100%;
    text-align: center;
    font-weight: 800;
    font-size: 58px;
    line-height: 1.08;
    letter-spacing: 1px;
    text-transform: uppercase;
    color: var(--ink-soft);
  }
  .contact-band {
    position: absolute;
    top: 494px;
    left: 0;
    width: 100%;
    height: 346px;
    background: linear-gradient(90deg,
      var(--silver-1) 0%, var(--silver-2) 14%, var(--silver-3) 30%,
      var(--silver-4) 48%, var(--silver-1) 64%, var(--silver-2) 82%, var(--silver-3) 100%);
    text-align: center;
  }
  .contact-name {
    position: absolute;
    top: 50px;
    width: 100%;
    font-weight: 700;
    font-size: 35px;
    letter-spacing: 0.5px;
  }
  .contact-icons {
    position: absolute;
    top: 106px;
    left: 187px;
    width: 119px;
    height: 36px;
    background: var(--ink);
    border-radius: 5px;
    display: flex;
    align-items: center;
    justify-content: space-around;
    padding: 0 12px;
  }
  .contact-icons svg { width: 26px; height: 24px; }
  .contact-line {
    position: absolute;
    width: 100%;
    font-size: 24px;
    font-weight: 400;
  }
  .contact-line--phone { top: 195px; }
  .contact-line--email { top: 226px; }
  .contact-rule {
    position: absolute;
    top: 310px;
    left: 69px;
    width: 355px;
    height: 12px;
    background: var(--ink);
  }

  /* Back */
  .pitch {
    position: absolute;
    top: 82px;
    left: 0;
    width: 100%;
    text-align: center;
    font-size: 20.5px;
    line-height: 26px;
  }
  .pitch-offer { margin-bottom: 30px; }
  .pitch-heading { font-weight: 700; text-transform: uppercase; padding: 0 40px; }
  .pitch-list { list-style: none; margin-top: 26px; }
  .deco-vertical {
    position: absolute;
    left: 32px;
    top: 512px;
    width: 18px;
    height: 328px;
    background: var(--ink);
  }
  .deco-horizontal {
    position: absolute;
    left: 60px;
    top: 751px;
    width: 119px;
    height: 18px;
    background: var(--ink);
  }
  .brand-watermark {
    position: absolute;
    left: 290px;
    top: 520px;
    font-weight: 800;
    font-size: 150px;
    line-height: 0.95;
    text-transform: uppercase;
    color: var(--brand-grey);
    white-space: nowrap;
  }
</style>
</head>
<body>
<main class="sheet">
  <section class="card card--front" aria-label="Card front">
    <div class="brand-mark">Kiosk<br>Coin<br>Venture</div>
    <div class="contact-band">
      <h1 class="contact-name">TOBIAS MERLANO</h1>
      <div class="contact-icons">
        <svg viewBox="0 0 24 24" aria-label="Phone" role="img">
          <path fill="#fff" d="M6.6 10.8a15 15 0 0 0 6.6 6.6l2.2-2.2c.3-.3.7-.4 1-.2 1.1.4 2.3.6 3.6.6.6 0 1 .4 1 1V20c0 .6-.4 1-1 1C10.6 21 3 13.4 3 4c0-.6.4-1 1-1h3.5c.6 0 1 .4 1 1 0 1.3.2 2.5.6 3.6.1.3 0 .7-.2 1z"/>
          <path fill="none" stroke="#fff" stroke-width="1.6" d="M14 6a4 4 0 0 1 4 4M14 2.5a7.5 7.5 0 0 1 7.5 7.5"/>
        </svg>
        <svg viewBox="0 0 26 20" aria-label="Email" role="img">
          <rect x="1" y="2" width="24" height="16" fill="none" stroke="#fff" stroke-width="1.8"/>
          <path d="M1 2l12 9 12-9M1 18l9-8M25 18l-9-8" fill="none" stroke="#fff" stroke-width="1.6"/>
        </svg>
      </div>
      <p class="contact-line contact-line--phone">(512) 638-9071</p>
      <p class="contact-line contact-line--email">Tobias@KioskCoin.example</p>
      <div class="contact-rule"></div>
    </div>
  </section>

  <section class="card card--back" aria-label="Card back">
    <div class="pitch">
      <p class="pitch-offer">$$$ FREE ATM PLACEMENT $$$</p>
      <h2 class="pitch-heading">Benifits of having an ATM at your business</h2>
      <p>FREE ATM and BTM (Bitcoin)<br>installation, maintenance, and<br>loading.</p>
      <ul class="pitch-list">
        <li>Lower card processing fees</li>
        <li>Stimulate more traffic.</li>
        <li>Ease of access for customers</li>
        <li>Maintain customers inside location.</li>
        <li>Higher tips and spending</li>
      </ul>
    </div>
    <div class="deco-vertical"></div>
    <div class="deco-horizontal"></div>
    <div class="brand-watermark" aria-hidden="true">Kiosk<br>Coin</div>
  </section>
</main>
</body>
</html>
```